Simple Floral Service Web-Banner

I need to put a banner add on the members section of a website for an organization in which we are members.

The ad size is 470px x 214px.

I am uploading 4 pictures. 1 is a picture of red roses, and 1 is a picture of a t-shirt. These are 2 major products of ours which need to be incorporated in the banner. I do not have these in higher res or vectorized format, so please work with what you have. I am also uploading our 2 logos, one is for our Canadian company, and one for our American company. Both logos should be included at equal sizes.

The following text should be used:
"Proudly providing top quality roses, and custom commemorative grad t-shirts at over 800 schools."

I am just looking for a simple banner incorporating those pictures and that wording. I don't want something that is overly flashy.

I will monitor the submissions in a timely manner and give you feedback.

```html
<!DOCTYPE html>
<html lang="en">
<head>
<meta charset="utf-8">
<title>Floral Service Web Banner</title>
<link href="https://fonts.googleapis.com/css2?family=Roboto+Condensed:wght@500;700&display=swap" rel="stylesheet">
<style>
  :root {
    --page-bg: #ffffff;
    --frame-line: #e4e4e4;
    --banner-dark: #4d7d2e;
    --banner-mid: #6fa033;
    --banner-bright: #8fc43c;
    --panel-bg: #fbfbd9;
    --brand-green: #6d9a2c;
    --headline: #ffffff;
    --shirt-light: #f4f4f2;
    --shirt-shade: #d3d5d0;
    --rose-bright: #d23a34;
    --rose-red: #b81a20;
    --rose-deep: #8e1217;
  }
  * { box-sizing: border-box; margin: 0; padding: 0; }
  html, body { width: 1200px; height: 1000px; overflow: hidden; background: var(--page-bg); }
  .canvas {
    position: relative; width: 1200px; height: 1000px;
    border: 1px solid var(--frame-line); border-radius: 4px;
  }
  .banner {
    position: absolute; left: 68px; top: 259px; width: 1067px; height: 485px;
    background:
      radial-gradient(ellipse 60% 80% at 68% 35%, var(--banner-bright) 0%, var(--banner-mid) 55%, transparent 100%),
      linear-gradient(90deg, var(--banner-dark) 0%, var(--banner-mid) 45%, var(--banner-bright) 100%);
    font-family: "Roboto Condensed", "Arial Narrow", sans-serif;
  }
  .brand-panel {
    position: absolute; left: 62px; top: 33px; width: 378px; height: 312px;
    background: var(--panel-bg); border-radius: 18px;
    padding: 14px 28px 0 20px; text-align: right; color: var(--brand-green);
  }
  .brand { display: flex; flex-direction: column; align-items: flex-end; font-weight: 700; line-height: 1; }
  .brand-line { font-size: 56px; letter-spacing: -0.5px; }
  .brand-line.second { display: flex; align-items: center; gap: 12px; margin-top: 6px; }
  .brand-dot { width: 18px; height: 18px; border-radius: 50%; background: var(--brand-green); }
  .brand-divider { height: 3px; background: var(--brand-green); margin: 14px -20px 16px 8px; }
  .product-shirts {
    position: absolute; left: 456px; top: 46px; width: 282px; height: 292px;
    background: linear-gradient(160deg, var(--shirt-light) 0%, var(--shirt-shade) 100%);
    border-radius: 12px;
  }
  .product-roses {
    position: absolute; left: 754px; top: 120px; width: 298px; height: 218px;
    background: linear-gradient(135deg, var(--rose-bright) 0%, var(--rose-red) 50%, var(--rose-deep) 100%);
    border-radius: 12px;
  }
  .headline {
    position: absolute; left: 0; right: 0; top: 370px;
    text-align: center; color: var(--headline); font-weight: 700;
    font-size: 40px; line-height: 43px; letter-spacing: 0.3px; text-transform: uppercase;
  }
</style>
</head>
<body>
  <div class="canvas">
    <section class="banner">
      <div class="brand-panel">
        <div class="brand">
          <span class="brand-line">Milestone</span>
          <span class="brand-line second"><span class="brand-dot"></span>Blooms</span>
        </div>
        <div class="brand-divider"></div>
        <div class="brand">
          <span class="brand-line">Cap &amp; Gown</span>
          <span class="brand-line second"><span class="brand-dot"></span>Florals</span>
        </div>
      </div>
      <div class="product-shirts" role="img" aria-label="Photo of two white commemorative graduation t-shirts, front with school name and back with graduating class list"></div>
      <div class="product-roses" role="img" aria-label="Photo of a wrapped bouquet of red roses with baby's breath and a red bow"></div>
      <p class="headline">Proudly providing top quality roses, and custom<br>commemorative grad t-shirts at over 800 schools.</p>
    </section>
  </div>
</body>
</html>
```